Business card design for new, innovative company - BluePlinth

We are a new company looking for a business card design that is fun, different and quirky. Must use corporate colour green - CMYK C:55, M:0, Y:100, K:0, and corporate colour grey - C:0, M:0, Y: 0, K:70.

We have developed the first real time data application, in which people are able to profile the data of their existing customers in order to pull out more good fit clients to direct their marketing activities at.

Industry/Entity Type

Marketing

Requirements
Must have
• Logo, name, title, telephone number, fax number, email, website, address

```html
<!DOCTYPE html>
<html lang="en">
<head>
<meta charset="utf-8">
<title>BluePlinth business card</title>
<link rel="stylesheet" href="https://fonts.googleapis.com/css2?family=Open+Sans:wght@400;600;700;800&display=swap">
<style>
  :root {
    --brand-green: #7cc242;
    --brand-grey: #6d6e71;
    --shape-grey: #58595b;
    --band-grey: #4b4c4e;
    --ink: #222222;
    --card-white: #ffffff;
    --backdrop: #9a9a9a;
  }
  * { box-sizing: border-box; margin: 0; padding: 0; }
  html, body { width: 1200px; height: 900px; overflow: hidden; }
  body {
    background: var(--backdrop);
    font-family: "Open Sans", sans-serif;
    position: relative;
  }
  .card {
    position: absolute;
    width: 580px;
    height: 340px;
    box-shadow: 0 10px 28px rgba(0,0,0,0.3);
    overflow: hidden;
  }

  /* Back of card */
  .card-back {
    left: 70px;
    top: 60px;
    background: var(--brand-grey);
  }
  .back-block {
    position: absolute;
    left: 70px;
    top: 40px;
    width: 260px;
    height: 260px;
    background: var(--shape-grey);
  }
  .card-back .wordmark {
    position: absolute;
    left: 100px;
    top: 130px;
    color: var(--card-white);
    font-size: 66px;
    font-weight: 800;
    letter-spacing: -2px;
    line-height: 1;
  }

  /* Front of card */
  .card-front {
    left: 550px;
    top: 500px;
    background: var(--card-white);
  }
  .card-front .wordmark {
    position: absolute;
    left: 30px;
    top: 18px;
    color: var(--brand-green);
    font-size: 50px;
    font-weight: 800;
    letter-spacing: -1.5px;
  }
  .front-block {
    position: absolute;
    left: 400px;
    top: 120px;
    width: 150px;
    height: 150px;
    background: var(--brand-grey);
  }
  .person {
    position: absolute;
    left: 38px;
    top: 104px;
  }
  .person-name {
    font-size: 20px;
    font-weight: 700;
    letter-spacing: 0.3px;
    text-transform: uppercase;
  }
  .first-name { color: var(--brand-green); }
  .last-name { color: var(--brand-grey); }
  .person-title {
    font-size: 12px;
    color: var(--ink);
  }
  .contact-list {
    position: absolute;
    left: 38px;
    top: 168px;
    list-style: none;
  }
  .contact-list li {
    display: flex;
    align-items: center;
    gap: 9px;
    font-size: 13.5px;
    color: var(--ink);
    height: 21px;
  }
  .contact-icon { width: 14px; height: 14px; flex: none; }
  .address-band {
    position: absolute;
    left: 0;
    bottom: 0;
    width: 100%;
    height: 70px;
    background: var(--band-grey);
    padding: 11px 0 0 38px;
    color: var(--brand-green);
    font-weight: 700;
    font-size: 14px;
    line-height: 22px;
    text-transform: uppercase;
  }
</style>
</head>
<body>

  <section class="card card-back" aria-label="Card back">
    <div class="back-block" aria-hidden="true"></div>
    <div class="wordmark">BluePlinth</div>
  </section>

  <section class="card card-front" aria-label="Card front">
    <div class="wordmark">BluePlinth</div>

    <div class="person">
      <div class="person-name"><span class="first-name">Nadia</span> <span class="last-name">Ferris</span></div>
      <div class="person-title">Director</div>
    </div>

    <ul class="contact-list">
      <li>
        <svg class="contact-icon" viewBox="0 0 14 14" aria-hidden="true"><rect width="14" height="14" rx="2" fill="var(--brand-green)"/><rect x="4.5" y="2.5" width="5" height="9" rx="1" fill="none" stroke="#fff" stroke-width="1.2"/></svg>
        079 5550 1842
      </li>
      <li>
        <svg class="contact-icon" viewBox="0 0 14 14" aria-hidden="true"><rect width="14" height="14" rx="2" fill="var(--brand-green)"/><path d="M4 3.5 L5.8 3.5 L6.4 5.6 L5.4 6.4 Q6.3 8.2 7.6 8.7 L8.4 7.7 L10.5 8.3 L10.5 10 Q6 10.5 4 3.5 Z" fill="#fff"/></svg>
        013 5550 2917
      </li>
      <li>
        <svg class="contact-icon" viewBox="0 0 14 14" aria-hidden="true"><rect width="14" height="14" rx="2" fill="var(--brand-green)"/><rect x="3" y="4.5" width="8" height="5.5" fill="none" stroke="#fff" stroke-width="1.1"/><path d="M3 4.5 L7 7.6 L11 4.5" fill="none" stroke="#fff" stroke-width="1.1"/></svg>
        nadia.ferris@northvaledistribution.com
      </li>
      <li>
        <svg class="contact-icon" viewBox="0 0 14 14" aria-hidden="true"><rect width="14" height="14" rx="2" fill="var(--brand-green)"/><rect x="3" y="3" width="8" height="8" fill="none" stroke="#fff" stroke-width="1.1"/><path d="M3 7 H11 M7 3 V11" stroke="#fff" stroke-width="1.1"/></svg>
        www.blueplinth.com
      </li>
    </ul>

    <div class="address-band">
      27A Kestrel Lane, Harbury<br>
      Warwickshire, CV33 9QT
    </div>

    <div class="front-block" aria-hidden="true"></div>
  </section>

</body>
</html>
```